Design the 21st Golden Reel Indie Screen Week Poster. Think modern, chic, cool, film, movies - driving people to the film festival - the film festivla is in San Francisco and the SF East Bay. Our logo is attached. Dates will be determined soon . please use - November 2 - 11, 2018 (for placement) Keep in mind abstract, chic, modern - eye catching. website is www.grisw.example

Target Market(s)

25 - 45 year old - upper middle class

Industry/Entity Type

Film Production

Colors

Designer to choose colors to be used in the design.

Requirements
Must have
• logo (attached) www.grisw.example - chic modern design
Nice to have
• best coolest poster ever!
Should not have
• CLIP ART!!!

```html
<!DOCTYPE html>
<html lang="en">
<head>
<meta charset="utf-8">
<title>21st Golden Reel Indie Screen Week</title>
<link rel="stylesheet" href="https://fonts.googleapis.com/css2?family=Bebas+Neue&family=Oswald:wght@300;400;500&display=swap">
<style>
  :root {
    --paper-light: #f1f1f1;
    --paper-mid: #dcdcdc;
    --paper-edge: #bdbdbd;
    --ink: #3a3a3a;
    --accent: #d0121a;
    --reel-light: #9a9a9a;
    --reel-dark: #141414;
  }
  html, body {
    margin: 0;
    padding: 0;
    width: 807px;
    height: 1200px;
    overflow: hidden;
  }
  .poster {
    position: relative;
    width: 807px;
    height: 1200px;
    overflow: hidden;
    background: radial-gradient(ellipse at 55% 45%, var(--paper-light) 0%, var(--paper-mid) 60%, var(--paper-edge) 100%);
    font-family: "Bebas Neue", "Oswald", sans-serif;
    color: var(--ink);
  }
  .reel-artwork {
    position: absolute;
    left: 300px;
    top: 100px;
    width: 400px;
    height: 540px;
  }
  .camera-artwork {
    position: absolute;
    left: 124px;
    top: 609px;
    width: 62px;
    height: 130px;
  }
  .tagline {
    position: absolute;
    margin: 0;
    font-family: "Oswald", sans-serif;
    font-weight: 400;
    font-size: 18px;
    line-height: 1;
    letter-spacing: 0.5px;
    text-transform: uppercase;
    white-space: nowrap;
  }
  .tagline em {
    font-style: italic;
    font-weight: 500;
    font-size: 22px;
    color: var(--accent);
  }
  .tagline-first { left: 234px; top: 680px; }
  .tagline-second { left: 302px; top: 702px; }
  .title { margin: 0; font-weight: 400; }
  .title span { position: absolute; line-height: 1; white-space: nowrap; }
  .edition {
    left: 124px;
    top: 728px;
    font-size: 186px;
    letter-spacing: -3px;
    color: var(--accent);
  }
  .name-first {
    left: 372px;
    top: 824px;
    font-size: 66px;
    letter-spacing: 1px;
  }
  .name-second {
    left: 128px;
    top: 893px;
    font-size: 49px;
    letter-spacing: 0.5px;
  }
  .name-third {
    left: 322px;
    top: 936px;
    font-size: 67px;
    letter-spacing: 1px;
  }
  .dates {
    position: absolute;
    margin: 0;
    left: 322px;
    white-space: nowrap;
    line-height: 1;
    font-family: "Oswald", sans-serif;
    font-weight: 300;
  }
  .dates-range {
    top: 1010px;
    font-size: 38px;
    letter-spacing: 9.5px;
    color: var(--accent);
  }
  .dates-year {
    top: 1060px;
    font-size: 42px;
    letter-spacing: 12px;
    color: var(--ink);
  }
  .website {
    position: absolute;
    margin: 0;
    left: 322px;
    top: 1128px;
    font-family: "Oswald", sans-serif;
    font-weight: 400;
    font-size: 18px;
    letter-spacing: 2px;
    line-height: 1;
    color: var(--ink);
    white-space: nowrap;
  }
</style>
</head>
<body>
<main class="poster">
  <svg class="reel-artwork" viewBox="0 0 400 540" role="img" aria-label="Abstract sphere formed by a spiralling strip of black film, floating above its shadow">
    <defs>
      <radialGradient id="reelTone" cx="40%" cy="35%" r="65%">
        <stop offset="0%" stop-color="var(--reel-light)"/>
        <stop offset="100%" stop-color="var(--reel-dark)"/>
      </radialGradient>
      <radialGradient id="reelShadow" cx="50%" cy="50%" r="50%">
        <stop offset="0%" stop-color="#555" stop-opacity="0.8"/>
        <stop offset="100%" stop-color="#555" stop-opacity="0"/>
      </radialGradient>
    </defs>
    <ellipse cx="198" cy="244" rx="172" ry="222" fill="url(#reelTone)"/>
    <ellipse cx="216" cy="520" rx="104" ry="16" fill="url(#reelShadow)"/>
  </svg>

  <svg class="camera-artwork" viewBox="0 0 62 130" role="img" aria-label="Small silhouette of a film camera on a tripod">
    <rect x="0" y="0" width="62" height="130" rx="6" fill="var(--reel-dark)" opacity="0.85"/>
  </svg>

  <p class="tagline tagline-first">Something for <em>everyone</em></p>
  <p class="tagline tagline-second">from around <em>the world</em></p>

  <h1 class="title">
    <span class="edition">21ST</span>
    <span class="name-first">GOLDEN REEL</span>
    <span class="name-second">INDIE SCREEN</span>
    <span class="name-third">WEEK</span>
  </h1>

  <p class="dates dates-range">NOVEMBER 2-11,</p>
  <p class="dates dates-year">2018</p>
  <p class="website">www.grisw.example</p>
</main>
</body>
</html>
```